Broschüre
Zielgruppe
Firmen und Privatpersonen
Unsere Zielkunden sind im bereich Firmen
Firmen die etwas für die Umwelt tun wollen oder sich einen Grünen anstrich geben wollen
Privatpersonen hier ist es die Gruppe die sich für den erhalt der Natur einsetzten die Bienen oder Naturprojekte unterstützen wollen und dergleichen. In der regel Menschen die BIO Kaufen
Aufgabenstellung
Standard Falzflyer DIN-A4 4 Seiten / Logo vorhanden / Unbedingt noch ein Freifeld zum ausfüllen zum bestellen. Daten die wir zum bestellen benötigen Name/Adresse/Telefonnummer/E-Mail/Unterschrift

```html
<!DOCTYPE html>
<html lang="de">
<head>
<meta charset="utf-8">
<title>Bienen auf Zeit – Innenseiten</title>
<link href="https://fonts.googleapis.com/css2?family=Crimson+Text:wght@400;600;700&display=swap" rel="stylesheet">
<style>
  :root {
    --band-yellow: #ffd966;
    --band-edge: #3a3320;
    --rule-gold: #f2b63a;
    --ink: #1c1a16;
    --field-line: #3a3320;
    --photo-cream: #f3ecdc;
    --photo-honey: #e8d7ab;
    --photo-sage: #d9e4bf;
    --photo-green: #c3d79a;
  }
  * { box-sizing: border-box; margin: 0; padding: 0; }
  html, body { width: 1200px; height: 800px; overflow: hidden; background: #fff; }
  .spread {
    position: relative;
    width: 1200px;
    height: 800px;
    font-family: "Crimson Text", Georgia, serif;
    color: var(--ink);
    overflow: hidden;
  }
  .bee-backdrop {
    position: absolute;
    inset: 48px 0 0 0;
    background:
      radial-gradient(ellipse at 18% 40%, rgba(232,215,171,.75), transparent 60%),
      radial-gradient(ellipse at 85% 70%, rgba(195,215,154,.8), transparent 60%),
      linear-gradient(100deg, var(--photo-cream) 0%, var(--photo-honey) 30%, var(--photo-sage) 65%, var(--photo-green) 100%);
  }
  .bee-backdrop::after {
    content: "";
    position: absolute;
    inset: 0;
    background: rgba(255,255,255,.45);
  }
  .top-band {
    position: absolute;
    left: 0; top: 0;
    width: 1200px; height: 48px;
    background: var(--band-yellow);
    border-bottom: 2px solid var(--band-edge);
  }
  .block { position: absolute; }
  .line {
    display: block;
    white-space: nowrap;
    text-align: justify;
    text-align-last: justify;
  }
  .line--end { text-align-last: left; }

  .column-title { font-weight: 400; font-size: 24px; }
  .intro-title { left: 50px; top: 64px; width: 348px; line-height: 33.5px; }
  .rescue-title { left: 419px; top: 63px; width: 348px; line-height: 31px; }
  .order-title { left: 786px; top: 68px; font-size: 22px; line-height: 28px; white-space: nowrap; }

  .body-copy {
    font-weight: 600;
    font-size: 17.6px;
    line-height: 22.5px;
    width: 348px;
  }
  .intro-copy { left: 50px; top: 200px; }
  .rescue-copy { left: 419px; top: 150px; }

  .divider {
    position: absolute;
    top: 68px;
    width: 2px;
    height: 662px;
    background: var(--rule-gold);
  }
  .divider--one { left: 409px; }
  .divider--two { left: 780px; }

  .small-copy { font-size: 13.6px; line-height: 18.5px; white-space: nowrap; }
  .option-list { list-style: none; left: 804px; top: 129px; }
  .option { display: flex; align-items: flex-start; gap: 10px; margin-bottom: 20px; }
  .option-box {
    flex: none;
    width: 21px; height: 21px;
    border: 2px solid var(--ink);
    margin-top: 3px;
  }
  .sponsor-intro { left: 786px; top: 266px; }
  .benefit-list { list-style: none; left: 786px; top: 303px; line-height: 18px; }

  .order-fields { left: 786px; top: 560px; width: 380px; }
  .field {
    display: flex;
    align-items: flex-end;
    gap: 8px;
    height: 31px;
    font-size: 13.6px;
  }
  .field-label { flex: none; width: 78px; line-height: 18px; }
  .field-line { flex: 1; border-bottom: 1px solid var(--field-line); height: 14px; margin-bottom: 4px; }

  .page-label { position: absolute; top: 757px; font-size: 13.6px; }
  .page-label--one { left: 50px; }
  .page-label--two { left: 421px; }
  .page-label--three { left: 790px; }
</style>
</head>
<body>
<div class="spread">
  <div class="bee-backdrop" role="img" aria-label="Hintergrundfoto: Bienen fliegen unscharf vor einem hellen Bienenstock und grünem Garten"></div>
  <div class="top-band"></div>

  <h2 class="block column-title intro-title">
    <span class="line">Werde Imker auf Zeit und miete</span>
    <span class="line">deinen eigenen Bienenstock voller</span>
    <span class="line line--end">fkeißiger Bestäuber</span>
  </h2>
  <p class="block body-copy intro-copy">
    <span class="line">Wollten Sie schon immer Imker werden und</span>
    <span class="line">eigenen Honig haben? Jetzt gibt es die Mög-</span>
    <span class="line">lichkeit in die Imkerei hinein zu schnuppern</span>
    <span class="line line--end">und einen Bienenstock für zwei Monate</span>
    <span class="line">(190 Euro) oder eine Saison (290 Euro) zu</span>
    <span class="line">„mieten“. Nach dieser Zeit gibt es den fix fer-</span>
    <span class="line">tig abgefüllten Honig „ihrer“ Bienen in 1-Ki-</span>
    <span class="line">lo-Gläsern. „Alles was das Bienenvolk im Ho-</span>
    <span class="line">nigraum sammelt gehört Ihnen“, und kann an</span>
    <span class="line">Ihre Liebsten und Freunde verschenkt wer-</span>
    <span class="line line--end">den.</span>
    <span class="line">Wer einen Blick in das faszinierende Trei-</span>
    <span class="line">ben seines Bienenvolk werfen möchte, hat</span>
    <span class="line">die Möglichkeit ein „Neugier-Paket“ dazu</span>
    <span class="line">zu nehmen, welches eine Imkerjacke, einen</span>
    <span class="line">Smoker und Handschuhe beinhaltet. „Da-</span>
    <span class="line">mit kann man jederzeit nachschauen, was die</span>
    <span class="line">Bienen so treiben. Natürlich gibt es auch eine</span>
    <span class="line line--end">Einschulung bei „Abholung“.</span>
  </p>

  <div class="divider divider--one"></div>

  <h2 class="block column-title rescue-title">
    <span class="line line--end">Bienenretter werden</span>
    <span class="line line--end">- leicht gemacht!</span>
  </h2>
  <p class="block body-copy rescue-copy">
    <span class="line">Mit den „Bienen auf Zeit“ kann man die Rol-</span>
    <span class="line">le des Beobachters gegen die des Machers</span>
    <span class="line">tauschen. „So kann man das Bienenvolk be-</span>
    <span class="line">obachten, begleiten und betreibt auch noch</span>
    <span class="line">aktiven Naturschutz. „Man muss nur darauf</span>
    <span class="line">achten den Bienenstock an einem nicht zu</span>
    <span class="line">windigen Platz aufzustellen“, und richtig aus-</span>
    <span class="line line--end">zurichten.</span>
    <span class="line">Aber auch zuhause im Garten kann man ei-</span>
    <span class="line">niges für die Bienen tun. Es ist oft leichter</span>
    <span class="line">als man glaubt, den kleinen Bienen zu hel-</span>
    <span class="line">fen in dem man Blumen und Sträucher setzt,</span>
    <span class="line">die alle Bestäuber lieben. Dazu gehören zum</span>
    <span class="line">Beispiel Schneeglöckchen, Krokus, Lavendel</span>
    <span class="line">oder Bohnenkraut um nur einige zu nen-</span>
    <span class="line">nen. Florana führt ein breites Sortiment an</span>
    <span class="line line--end">Pflanzen, die unsere Bienen lieben.</span>
    <span class="line">„Gemeinschaftlich können wir zeigen, was</span>
    <span class="line">nötig und möglich ist, um Österreich wie-</span>
    <span class="line">der bienenfreundlicher zu machen. Helfen</span>
    <span class="line">Sie mit, den Bienen vielfältige und abwechs-</span>
    <span class="line">lungsreiche Lebensräume bereitzustellen und</span>
    <span class="line line--end">deren Überleben zu sichern.</span>
  </p>

  <div class="divider divider--two"></div>

  <h2 class="block column-title order-title">Ja, ich möchte helfen und bestelle:</h2>
  <ul class="block option-list small-copy">
    <li class="option"><span class="option-box"></span><span>Bienenvolk zur Miete für 2 Monate zu einer<br>Pauschale von 190€</span></li>
    <li class="option"><span class="option-box"></span><span>Bienenvolk zur Miete für 1 Saison zu einer<br>Pauschale von 290€</span></li>
  </ul>
  <p class="block sponsor-intro small-copy">Für die Bienenpatenschaft über 1 Saison erhalte ich:</p>
  <ul class="block benefit-list small-copy">
    <li>• Die Summwerk´s stellt Ihren Bienenstock auf den Fel-<br>dern des umgewidmet Projektes auf.</li>
    <li>• Die Summwerk´s kümmert sich um die Pflege und erntet<br>den Honig.</li>
    <li>• Die Summwerk´s informiert Sie über Leben und Arbeit<br>Ihrer Bienen.</li>
    <li>• Sie übernehmen die Patenschaft um jährlich 290 Euro<br>pro Bienenstock.</li>
    <li>• Sie können Ihrem Bienenvolk und Ihrer Königin einen<br>Namen geben.</li>
    <li>• Sie bekommen jährlich 6 kg Honig und 2 Flaschen<br>Honigwein Ihres Bienenvolkes.</li>
  </ul>

  <div class="block order-fields">
    <div class="field"><span class="field-label">Name:</span><span class="field-line"></span></div>
    <div class="field"><span class="field-label">Adresse:</span><span class="field-line"></span></div>
    <div class="field"><span class="field-label">Telefon:</span><span class="field-line"></span></div>
    <div class="field"><span class="field-label">E-Mail:</span><span class="field-line"></span></div>
    <div class="field"><span class="field-label">Unterschrift:</span><span class="field-line"></span></div>
  </div>

  <span class="page-label page-label--one">Innenseite</span>
  <span class="page-label page-label--two">Innenseite</span>
  <span class="page-label page-label--three">Rückseite Bestellfomular</span>
</div>
</body>
</html>
```